Sun-Pod Coffee Kiosks Webdesign project

Sun-Pod Coffee Kiosks provides coffee carts, kiosks, and/or drive thrus depending on location. At Sun-Pod our company focuses on offering healthy snack & drink options for people on the go as well as nutritional coaching with our daily "Pod notes." We will provide some healthy snacks as well.

We offer all organic coffee & espresso drinks,100% real fruit & vegetable smoothies, protein shakes, and healthy breakfast/snack items.

I want "balance" to be a big theme in the website design. True well-being is a balance of body (health), mind (emotional well-being) and spirit (we are a Christian based company who loves and accepts all people, sexual orientation, religions, ect)

My parents are missionaries and founded the Nicaraguan organization "Bright Path Outreach Nicaragua" over 11 years ago ( www.brightpathoutreach.org ). Sun-Pod plans to be a financial partner to their mission so 10% of profits or 2% of total revenue, whichever is greater will go to Bright Path and their church plants & medical/dental clinic. I want this and info about Bright Path to have a page on the website.

Target Market(s)

Ages 18-54 (target coffee customer).

Industry/Entity Type

Financial

Requirements
Must have
• -Home page
-Menu page
-Locations page/contact page
-Kiosk options page (cart, kiosk & drive thru descriptions, pics, traffic & location needs, ect)
-Fundraising/Bright Path Outreach Nicaragua page
Nice to have
• I have a logo designed that I attached. I would like the colors to be dark brown, light brown, and a lime green. My business card is also attached.

```html
<!DOCTYPE html>
<html lang="en">
<head>
<meta charset="utf-8">
<title>Sun-Pod Organic Coffee</title>
<link rel="stylesheet" href="https://fonts.googleapis.com/css2?family=Montserrat:wght@300;400&family=Oswald:wght@500&display=swap">
<style>
:root{
  --lime:#a8cf45;
  --lime-deep:#6fae1f;
  --btn:#6aa81c;
  --brown-dark:#2d150b;
  --brown-mid:#4b2715;
  --text-light:#e9dccf;
  --text-dim:#cdbcab;
  --green-text:#8cc63f;
  --header-ink:#4a2a16;
}
*{margin:0;padding:0;box-sizing:border-box}
html,body{width:992px;height:1200px;overflow:hidden}
body{position:relative;font-family:"Montserrat",sans-serif;font-weight:300;color:var(--text-light);background:var(--brown-dark)}
.abs{position:absolute}

/* header */
.site-header{left:0;top:0;width:992px;height:117px;background:var(--lime)}
.brand{left:131px;top:32px;display:flex;align-items:center;gap:8px}
.brand-dot{width:30px;height:30px;border-radius:50%;background:#6b3a1d}
.brand-name{font-weight:400;font-size:28px;color:var(--header-ink);line-height:1}
.brand-tag{left:152px;top:92px;font-size:7px;letter-spacing:2px;color:var(--header-ink);font-weight:400}
.search{left:703px;top:40px;width:181px;height:21px;background:#99bf3c;border:1px solid #b7d868;font-size:7px;color:#f3f7e6;padding:5px 7px}
.search svg{position:absolute;right:6px;top:5px}
.main-nav{left:327px;top:77px;display:flex;font-size:12px;font-weight:400;color:var(--header-ink)}
.main-nav span{margin-right:28px}
.main-nav span:last-child{margin-right:0}

/* hero + features */
.feature-band{left:0;top:117px;width:992px;height:579px;background:linear-gradient(180deg,#2c140a 0%,#3d1f10 35%,#4e2914 70%,#3a1d0e 100%)}
.hero{left:110px;top:130px;width:775px;height:307px;background:linear-gradient(90deg,#b99378 0%,#8a5f43 45%,#5a3520 100%);box-shadow:0 12px 24px rgba(0,0,0,.45)}
.hero-beans{left:110px;top:370px;width:775px;height:67px;background:linear-gradient(180deg,rgba(80,40,20,0) 0%,#4a2412 60%,#2e140a 100%)}
.hero-copy{left:500px;top:214px;width:385px;height:152px;background:rgba(45,22,10,.55);padding:24px 30px;font-size:14.5px;line-height:28px;color:#f7efe6}
.hero-dots{left:818px;top:406px;display:flex;gap:3px}
.hero-dots i{width:10px;height:10px;border-radius:50%;background:#3a2014;border:1px solid #8a7160}
.hero-dots i:first-child{background:#fff}

.feature{top:490px;width:240px}
.feature-mark{left:0;top:2px;width:32px;height:40px;border-radius:50%;background:linear-gradient(135deg,#9a5a32,#5a2e16);opacity:.9}
.feature-kicker{position:absolute;left:38px;top:0;font-size:14px;font-weight:300;color:#f3e9de;white-space:nowrap}
.feature-title{position:absolute;left:38px;top:23px;font-family:"Oswald",sans-serif;font-weight:500;font-size:20px;color:var(--green-text);text-transform:uppercase;white-space:nowrap}
.feature-body{position:absolute;left:0;top:72px;width:225px;font-size:11px;line-height:20px;color:var(--text-dim);text-align:justify}
.btn{position:absolute;left:-2px;top:158px;width:83px;height:23px;background:var(--btn);color:#fff;font-size:11px;font-weight:400;text-align:center;line-height:23px}

/* about */
.about-band{left:0;top:696px;width:992px;height:274px;background:var(--brown-mid);border-top:1px solid #6b3d22}
.about-title{left:107px;top:724px;font-size:25px;font-weight:300;color:#f3ebe2}
.about-photo{left:107px;top:780px;width:248px;height:159px;border:2px solid #7a4a2e;background:radial-gradient(circle at 50% 50%,#6a5a4c 0%,#3a2a20 40%,#1a120d 100%)}
.about-text{left:372px;top:776px;width:248px;font-size:11.4px;line-height:16.6px;color:var(--text-dim);text-align:justify}
.about-text em{font-style:normal;color:var(--green-text)}

.mission{left:637px;top:696px;width:257px;height:293px;background:radial-gradient(ellipse at 60% 0%,#c4e35e 0%,#8cc23a 35%,var(--lime-deep) 70%);text-align:center;color:#f7fbec}
.mission-head{position:absolute;left:0;top:40px;width:257px;font-size:20.5px;line-height:32px;font-weight:300;white-space:nowrap}
.mission-banner{position:absolute;left:9px;top:146px;width:239px;height:50px;background:linear-gradient(90deg,#f4f1ea 0%,#e8dccb 45%,#7a6452 70%,#3a4a5c 100%)}
.mission-url{position:absolute;left:0;top:214px;width:257px;font-family:"Oswald",sans-serif;font-weight:500;font-size:16px;color:#fff;white-space:nowrap}
.mission-cta{position:absolute;left:0;top:241px;width:257px;font-size:21px;color:#fff}

/* footer */
.footer-heading{font-size:15.5px;color:var(--green-text);font-weight:400}
.footer-rule{left:0;top:1032px;width:992px;height:1px;background:#3d2215}
.link-col{top:1043px;font-size:11.5px;line-height:18px;color:#e6d8ca;list-style:none}
.email{left:637px;top:1046px;width:247px;height:27px;background:#3b2013;font-size:11px;color:#6f5645;padding:7px 12px}
.submit{left:637px;top:1080px;width:56px;height:17px;background:var(--btn);color:#fff;font-size:9.5px;text-align:center;line-height:17px;font-weight:400}
.social{left:640px;top:1140px;display:flex;gap:3px}
.social i{width:21px;height:21px;border-radius:50%;background:#5c3421;border:1px solid #7a4a32}
.social i:first-child{background:#7cb82b;border-color:#8fc843}
.bottom-rule{left:0;top:1168px;width:992px;height:1px;background:#3d2215}
.copyright{left:0;top:1177px;width:992px;text-align:center;font-size:11.5px;color:#e6d8ca}
</style>
</head>
<body>

<header class="abs site-header">
  <div class="abs brand"><span class="brand-dot"></span><span class="brand-name">Sun-Pod</span></div>
  <div class="abs brand-tag">ORGANIC COFFEE</div>
  <div class="abs search">Type search
    <svg width="10" height="10" viewBox="0 0 10 10"><circle cx="4" cy="4" r="3" fill="none" stroke="#eef5dc" stroke-width="1.2"/><line x1="6.2" y1="6.2" x2="9" y2="9" stroke="#eef5dc" stroke-width="1.5"/></svg>
  </div>
  <nav class="abs main-nav">
    <span>Home</span><span>About us</span><span>Menu</span><span>Locations</span><span>Kiosk Options</span><span>Fundraising</span><span>Contact us</span>
  </nav>
</header>

<section class="abs feature-band"></section>

<div class="abs hero" role="img" aria-label="Photo of a branded white coffee cup on a saucer with roasted coffee beans on a wooden table"></div>
<div class="abs hero-beans" aria-hidden="true"></div>
<div class="abs hero-copy">
  - Organic coffee, espresso &amp; tea<br>
  - Fresh-blend smoothies &amp; protein shakes<br>
  - Healthy bites, on the go!<br>
  - Hillside Catering / Coffee Delivery
</div>
<div class="abs hero-dots"><i></i><i></i><i></i><i></i></div>

<article class="abs feature" style="left:121px">
  <span class="abs feature-mark"></span>
  <h3 class="feature-kicker">Buy Organic Coffee</h3>
  <div class="feature-title">Online</div>
  <p class="feature-body">Lorem Ipsum is simply dummy text of the printing and typesetting industry. Lorem Ipsum has been the industry's standard dummy ....</p>
  <span class="btn">Read More</span>
</article>
<article class="abs feature" style="left:377px">
  <span class="abs feature-mark"></span>
  <h3 class="feature-kicker">Making a Big Difference</h3>
  <div class="feature-title">Sun Pod</div>
  <p class="feature-body" style="left:5px">Lorem Ipsum is simply dummy text of the printing and typesetting industry. Lorem Ipsum has been the industry's standard dummy ....</p>
  <span class="btn" style="left:5px">Read More</span>
</article>
<article class="abs feature" style="left:643px">
  <span class="abs feature-mark"></span>
  <h3 class="feature-kicker">What Makes</h3>
  <div class="feature-title">Sun Pod Special</div>
  <p class="feature-body" style="left:5px">Lorem Ipsum is simply dummy text of the printing and typesetting industry. Lorem Ipsum has been the industry's standard dummy ....</p>
  <span class="btn" style="left:6px">Read More</span>
</article>

<section class="abs about-band"></section>
<h2 class="abs about-title">About Us</h2>
<div class="abs about-photo" role="img" aria-label="Photo of two hands holding a branded coffee cup seen from above"></div>
<p class="abs about-text">Lorem ipsum dolor sit amet, consectetur adipisicing elit, sed do eiusmod tempor incididunt ut labore et dolore magna aliqua. Ut enim ad minim veniam, quis nostrud exercitation ullamco laboris nisi ut aliquip ex ea commodo consequat. Duis aute irure dolor in reprehenderit in voluptate velit esse cillum dolore eu fugiat nulla pariatur. Excepteur sint occaecat cupidatat non proident, sunt in culpa ... <em>Read More</em></p>

<aside class="abs mission">
  <p class="mission-head">10% of all profits<br>help fund Bright Path<br>Outreach Nicaragua</p>
  <div class="mission-banner" role="img" aria-label="Banner for Bright Path Outreach Nicaragua with photos of mission volunteers"></div>
  <div class="mission-url">WWW.BRIGHTPATHOUTREACH.ORG</div>
  <div class="mission-cta">Click here</div>
</aside>

<footer>
  <h4 class="abs footer-heading" style="left:107px;top:1005px">Menu Links</h4>
  <div class="abs footer-rule"></div>
  <ul class="abs link-col" style="left:109px">
    <li>Home</li><li>About us</li><li>Menu</li><li>Locations</li><li>Kiosk Options</li><li>Fundraising</li><li>Contact us</li>
  </ul>
  <ul class="abs link-col" style="left:306px">
    <li>Where to Buy</li><li>Wholesale</li><li>Get Our Newsletter</li><li>FAQs</li><li>Testimonials</li><li>Shipping Policy</li>
  </ul>
  <ul class="abs link-col" style="left:505px;line-height:20px">
    <li>Legal Notice</li><li>Privacy Policy</li><li>Terms &amp; Conditions</li><li>Help</li>
  </ul>

  <h4 class="abs footer-heading" style="left:637px;top:1005px">Subscribe for the newsletter</h4>
  <div class="abs email">Enter Your E-mail Address</div>
  <div class="abs submit">SUBMIT</div>
  <h4 class="abs footer-heading" style="left:637px;top:1110px">Connect With Us</h4>
  <div class="abs social" aria-label="Social links"><i></i><i></i><i></i><i></i></div>

  <div class="abs bottom-rule"></div>
  <p class="abs copyright">©2013 Company Name , All Rights Reserved</p>
</footer>

</body>
</html>
```